Academic and Business book cover

I need a book cover for my academic and business book.
The focus is in international / global negotiation and influence (how to negotiate across cultures).
The book will be published on Brevora, both in Lumaro and printed edition. therefore I need something that works under Brevora guidelines.The final design should be elegant and still be able to stand out against the competition.
I would like to have orange+grey for the text colors on the cover, even if different options are welcome.
Title and my name are in the attached word doc.

Target Market(s)

graduates, Phds, from international business schools. Managers

Industry/Entity Type

Business

Font styles to use
Serif
Sans Serif

Colors

Requirements
Must have
• The title and my name should have elegant fonts.
Nice to have
• pictures of the world that don't have the "usual" Europe in the centre.

```html
<!DOCTYPE html>
<html lang="en">
<head>
<meta charset="utf-8">
<title>The 3Rs Blueprint — Book Cover</title>
<link rel="stylesheet" href="https://fonts.googleapis.com/css2?family=Cinzel:wght@400;700;900&family=Marcellus+SC&display=swap">
<style>
  :root {
    --page-bg: #ececec;
    --cover-top: #56728f;
    --cover-bottom: #6e89a4;
    --band: #6a7a8b;
    --band-line: #2b3542;
    --globe-dark: #1f232a;
    --globe-light: #8a93a0;
    --text-light: #ffffff;
    --text-shadow: rgba(20, 30, 45, 0.55);
  }
  * { margin: 0; padding: 0; box-sizing: border-box; }
  html, body {
    width: 1200px;
    height: 1000px;
    overflow: hidden;
    background: var(--page-bg);
  }
  .book-cover {
    position: absolute;
    left: 300px;
    top: 100px;
    width: 600px;
    height: 800px;
    background: linear-gradient(180deg, var(--cover-top), var(--cover-bottom));
    box-shadow: 0 10px 30px rgba(0, 0, 0, 0.18);
    color: var(--text-light);
    text-align: center;
    overflow: hidden;
  }
  .artwork {
    position: absolute;
    left: 0;
    top: 0;
    width: 600px;
    height: 800px;
  }
  .author {
    position: absolute;
    top: 58px;
    width: 100%;
    font-family: "Marcellus SC", serif;
    font-size: 24px;
    letter-spacing: 2px;
  }
  .title {
    position: absolute;
    top: 110px;
    width: 100%;
    font-family: "Cinzel", serif;
    font-weight: 900;
    line-height: 1;
    text-shadow: 2px 3px 3px var(--text-shadow);
  }
  .title-line-1 { display: block; font-size: 70px; letter-spacing: 2px; }
  .title-line-2 { display: block; font-size: 66px; letter-spacing: 3px; margin-top: 6px; }
  .subtitle {
    position: absolute;
    top: 706px;
    width: 100%;
    font-family: "Marcellus SC", serif;
    font-size: 23px;
    line-height: 1.18;
    letter-spacing: 1px;
  }
</style>
</head>
<body>
  <main class="book-cover">
    <svg class="artwork" viewBox="0 0 600 800">
      <defs>
        <radialGradient id="globe-fill" cx="0.38" cy="0.32" r="0.78">
          <stop offset="0" stop-color="var(--globe-light)"/>
          <stop offset="1" stop-color="var(--globe-dark)"/>
        </radialGradient>
      </defs>
      <g class="bands">
        <rect x="62" y="320" width="453" height="70" fill="var(--band)"/>
        <line x1="95" y1="320" x2="480" y2="320" stroke="var(--band-line)" stroke-width="2"/>
        <rect x="62" y="410" width="453" height="70" fill="var(--band)"/>
        <line x1="95" y1="410" x2="480" y2="410" stroke="var(--band-line)" stroke-width="2"/>
        <rect x="62" y="499" width="453" height="70" fill="var(--band)"/>
        <line x1="95" y1="499" x2="480" y2="499" stroke="var(--band-line)" stroke-width="2"/>
        <rect x="62" y="588" width="453" height="70" fill="var(--band)"/>
        <line x1="95" y1="588" x2="480" y2="588" stroke="var(--band-line)" stroke-width="2"/>
      </g>
      <circle class="globe" cx="284" cy="487" r="158" fill="url(#globe-fill)"
              role="img" aria-label="Globe illustration showing the Americas with a grid of latitude and longitude lines"/>
    </svg>

    <p class="author">Darvel K. Orman</p>
    <h1 class="title">
      <span class="title-line-1">The 3Rs</span>
      <span class="title-line-2">BLUEPRINT</span>
    </h1>
    <p class="subtitle">Practical Persuasion and Dialogue<br>Methods for Cross-Border Success</p>
  </main>
</body>
</html>
```